Aerospace Center needs app design

We need a design that would be a creative and innovative look of a simple idea connecting air traffic control situations with sonification.
We would like to see designs that use the elements shown in the short video which are different pads, showing 4 different colors, connecting with a degree and feeling of urgency. The different pads will be movable over screen, similar as to a whiteboard where you can move things around. Each of those pads has 4 different elements that are shown:
- ATC Event (you can chose different setups)
- Select a status (you can chose between Information, Caution and Alert. Color needs to feel more alert from Information to Alert.
- Notes box (you can open the box and write additional text on it)
- Music (you can chose different files. on the right side you can see a small group of notes. When you hover over the notes, music will be played without pressing a play or stop button.
The second video is an overview of music archival program that is connected with the pads.
Look and feel
Each slider illustrates characteristics of the customer's brand and the style your logo design should communicate.

```html
<!DOCTYPE html>
<html lang="en">
<head>
<meta charset="utf-8">
<title>SKYNOTE – ATC Sonification Pads</title>
<link href="https://fonts.googleapis.com/css2?family=Hind:wght@400;500;700&display=swap" rel="stylesheet">
<style>
  :root{
    --header-a:#5ec3da;
    --header-b:#0d8fdc;
    --sidebar:#128fe0;
    --sidebar-active:#4fc0dc;
    --white:#ffffff;
    --field-text:#3d3d3d;
    --caret:#333;
    --info-outer-a:#0f86dc;
    --info-outer-b:#3db3f2;
    --info-panel:rgba(98,196,220,.93);
    --info-scene:#6fc4f6;
    --yellow-outer-a:#ff5e5e;
    --yellow-outer-b:#ffb624;
    --yellow-panel:#fcc416;
    --yellow-scene:#e8b21a;
    --green-outer-a:#3c7360;
    --green-outer-b:#5fd12c;
    --green-panel:#74d62b;
    --green-scene:#52c227;
    --red-outer-a:#9c0000;
    --red-outer-b:#ea0000;
    --red-panel:#ee0202;
    --red-scene:#ff6b6b;
    --gold:#f2c12e;
    --tower-blue:#57c2dc;
    --tower-navy:#0c6fbf;
    --footer:#222;
  }
  *{box-sizing:border-box;margin:0;padding:0}
  html,body{width:1200px;height:597px;overflow:hidden;background:var(--white);font-family:"Hind",sans-serif}
  .canvas{position:relative;width:1200px;height:597px;overflow:hidden;background:var(--white)}

  /* header */
  .topbar{position:absolute;left:0;top:0;width:1200px;height:52px;background:linear-gradient(180deg,var(--header-a),var(--header-b))}
  .brand{position:absolute;left:26px;top:11px;color:var(--white);font-weight:700;font-size:24px;letter-spacing:1px;line-height:30px}
  .search{position:absolute;left:652px;top:11px;width:271px;height:27px;border-radius:14px;background:#f2f4f6;color:#8a8f95;font-size:10px;line-height:28px;padding-left:12px}
  .search svg{position:absolute;right:12px;top:8px}
  .mode-toggle{position:absolute;left:955px;top:18px;width:31px;height:14px;border-radius:7px;background:var(--white)}
  .mode-toggle::after{content:"";position:absolute;right:2px;top:2px;width:10px;height:10px;border-radius:50%;background:#4fc0dc}
  .bell{position:absolute;left:996px;top:18px}
  .user-avatar{position:absolute;left:1034px;top:10px;width:30px;height:30px;border-radius:50%;background:linear-gradient(160deg,#c9b6a6,#5c5046)}
  .user-avatar::after{content:"";position:absolute;right:-1px;top:0;width:7px;height:7px;border-radius:50%;background:#29e25a}
  .user-name{position:absolute;left:1073px;top:18px;color:var(--white);font-size:10px;font-weight:500;letter-spacing:.5px}

  /* sidebar */
  .sidebar{position:absolute;left:0;top:67px;width:50px;height:540px;background:var(--sidebar);border-top-right-radius:26px}
  .nav-icon{position:absolute;left:13px;width:14px;height:14px}
  .nav-active{position:absolute;left:6px;top:19px;width:30px;height:30px;border-radius:50%;background:var(--sidebar-active)}
  .side-avatar{position:absolute;left:6px;top:345px;width:32px;height:32px;border-radius:50%;background:linear-gradient(160deg,#c9b6a6,#5c5046)}
  .side-avatar::after{content:"";position:absolute;right:0;top:1px;width:7px;height:7px;border-radius:50%;background:#29e25a}

  /* connecting route */
  .route{position:absolute;left:0;top:0}

  /* pads */
  .pad{position:absolute;top:178px;width:216px;height:353px;border-radius:108px 108px 10px 10px;overflow:visible}
  .pad-body{position:absolute;inset:0;border-radius:108px 108px 10px 10px;overflow:hidden}
  .pad-scene{position:absolute;left:0;bottom:0;width:100%;height:150px}
  .pad-panel{position:absolute;left:20px;top:14px;width:177px;height:232px;border-radius:30px}
  .pad--info .pad-panel{top:-12px;border-radius:30px}
  .field{position:absolute;left:13px;width:149px;height:30px;border-radius:15px;background:var(--white);color:var(--field-text);font-size:10px;line-height:31px;padding-left:14px}
  .field--select::after{content:"";position:absolute;right:12px;top:13px;border-left:4px solid transparent;border-right:4px solid transparent;border-top:4px solid var(--caret)}
  .field:nth-child(1){top:16px}
  .field:nth-child(2){top:53px}
  .field:nth-child(3){top:90px}
  .field:nth-child(4){top:128px}
  .sound-btn{position:absolute;left:66px;top:170px;width:46px;height:46px;border-radius:50%;display:flex;align-items:center;justify-content:center}
  .tower{position:absolute;width:46px;height:46px;border-radius:50%;display:flex;align-items:center;justify-content:center}

  .pad--info{left:95px}
  .pad--info .pad-body{background:linear-gradient(180deg,var(--info-outer-a),var(--info-outer-b))}
  .pad--info .pad-scene{background:linear-gradient(180deg,var(--info-outer-b),var(--info-scene) 55%,#2f8fe0)}
  .pad--info .pad-panel{background:var(--info-panel);box-shadow:0 6px 14px rgba(0,60,120,.25)}
  .pad--info .sound-btn{background:var(--gold);box-shadow:0 0 0 4px rgba(242,193,46,.35)}

  .pad--landing{left:379px}
  .pad--landing .pad-body{background:linear-gradient(180deg,var(--yellow-outer-a),var(--yellow-outer-b))}
  .pad--landing .pad-scene{background:linear-gradient(180deg,var(--yellow-outer-b),var(--yellow-scene) 60%,#b99015)}
  .pad--landing .pad-panel{background:var(--yellow-panel)}
  .pad--landing .sound-btn{background:var(--tower-blue);box-shadow:0 0 0 4px rgba(87,194,220,.35)}

  .pad--departure{left:660px}
  .pad--departure .pad-body{background:linear-gradient(180deg,var(--green-outer-a),var(--green-outer-b))}
  .pad--departure .pad-scene{background:linear-gradient(180deg,var(--green-outer-b),var(--green-scene) 60%,#3d9a1c)}
  .pad--departure .pad-panel{background:var(--green-panel)}
  .pad--departure .sound-btn{background:var(--tower-navy);box-shadow:0 0 0 4px rgba(12,111,191,.35)}

  .pad--alert{left:941px}
  .pad--alert .pad-body{background:linear-gradient(180deg,var(--red-outer-a),var(--red-outer-b))}
  .pad--alert .pad-scene{background:linear-gradient(180deg,var(--red-outer-b),var(--red-scene) 60%,#e60000)}
  .pad--alert .pad-panel{background:var(--red-panel)}
  .pad--alert .sound-btn{background:var(--gold);box-shadow:0 0 0 4px rgba(242,140,46,.5)}

  .footer{position:absolute;left:0;width:1200px;top:558px;padding-left:50px;text-align:center;font-size:8.5px;color:var(--footer)}
</style>
</head>
<body>
<div class="canvas">

  <header class="topbar">
    <div class="brand">SKYNOTE</div>
    <div class="search">Search
      <svg width="9" height="9" viewBox="0 0 10 10"><circle cx="4" cy="4" r="3" fill="none" stroke="#222" stroke-width="1.6"/><line x1="6.3" y1="6.3" x2="9.2" y2="9.2" stroke="#222" stroke-width="1.6"/></svg>
    </div>
    <div class="mode-toggle"></div>
    <svg class="bell" width="10" height="11" viewBox="0 0 10 11"><path d="M5 0.5c-2 0-3 1.5-3 3.5v2.5L1 8h8L8 6.5V4c0-2-1-3.5-3-3.5z" fill="#fff"/><circle cx="5" cy="9.5" r="1.2" fill="#fff"/></svg>
    <div class="user-avatar" role="img" aria-label="User profile photo"></div>
    <div class="user-name">ALEX MORAN</div>
  </header>

  <nav class="sidebar">
    <div class="nav-active"></div>
    <svg class="nav-icon" style="top:27px;left:14px" viewBox="0 0 14 14"><path d="M7 1L1 7h2v6h3V9h2v4h3V7h2z" fill="#fff"/></svg>
    <svg class="nav-icon" style="top:73px" viewBox="0 0 14 14"><path d="M3 1l2.5 3-1.5 1.5c.8 1.8 2.2 3.2 4 4L9.5 8 13 10.5 11.5 13C6 12.5 1.5 8 1 2.5z" fill="#fff"/></svg>
    <svg class="nav-icon" style="top:119px" viewBox="0 0 14 14"><path d="M7 1L1 7h2v6h3V9h2v4h3V7h2z" fill="#fff"/></svg>
    <svg class="nav-icon" style="top:166px" viewBox="0 0 14 14"><circle cx="7" cy="4" r="3" fill="#fff"/><path d="M2 13c0-4 2-5.5 5-5.5s5 1.5 5 5.5z" fill="#fff"/></svg>
    <svg class="nav-icon" style="top:212px" viewBox="0 0 14 14"><path d="M1 1v12h12" fill="none" stroke="#fff" stroke-width="1.4"/><rect x="3.5" y="7" width="1.6" height="5" fill="#fff"/><rect x="6" y="4" width="1.6" height="8" fill="#fff"/><rect x="8.5" y="6" width="1.6" height="6" fill="#fff"/><rect x="11" y="3" width="1.6" height="9" fill="#fff"/></svg>
    <svg class="nav-icon" style="top:258px" viewBox="0 0 14 14"><circle cx="5" cy="8" r="3.6" fill="none" stroke="#fff" stroke-width="2.4" stroke-dasharray="2 1.3"/><circle cx="11" cy="3.5" r="2" fill="none" stroke="#fff" stroke-width="1.6" stroke-dasharray="1.4 1"/><circle cx="11" cy="11" r="1.8" fill="none" stroke="#fff" stroke-width="1.5" stroke-dasharray="1.4 1"/></svg>
    <svg class="nav-icon" style="top:304px" viewBox="0 0 14 14"><path d="M2 1h7l3 3v9H2z" fill="#fff"/><path d="M4 7h6M4 9h6M4 11h6" stroke="#128fe0" stroke-width="1"/></svg>
    <div class="side-avatar" role="img" aria-label="User profile photo"></div>
  </nav>

  <svg class="route" width="1200" height="597" viewBox="0 0 1200 597" fill="none">
    <path d="M203 167 C235 130 290 125 320 155" stroke="#1a86d8" stroke-width="1.8" stroke-dasharray="4 4"/>
    <path d="M198 160 l6 8 l3-9" stroke="#1a86d8" stroke-width="1.6"/>
    <path d="M320 155 C345 185 370 200 395 175 S440 120 478 145" stroke="#c05a8a" stroke-width="1.8" stroke-dasharray="4 4"/>
    <path d="M505 145 C540 128 575 125 600 150 S640 195 665 180 S715 125 760 140" stroke="#e2465a" stroke-width="1.8" stroke-dasharray="4 4"/>
    <path d="M795 140 C835 120 870 120 895 145 S930 190 955 170 S1020 110 1060 140" stroke="#7a1022" stroke-width="1.8" stroke-dasharray="4 4"/>
  </svg>

  <!-- Pad 1: empty setup -->
  <section class="pad pad--info">
    <div class="pad-body"><div class="pad-scene" role="img" aria-label="Illustration of an airliner over an airport terminal and city skyline in blue tones"></div></div>
    <div class="pad-panel">
      <div class="field field--select">Select atc event</div>
      <div class="field field--select">Select status Level</div>
      <div class="field">Notes</div>
      <div class="field field--select">Select sound file</div>
      <div class="sound-btn"><svg width="22" height="20" viewBox="0 0 22 20" fill="none" stroke="#222" stroke-width="1.4"><path d="M6 15V3l4 3"/><ellipse cx="4" cy="15" rx="2.2" ry="1.7"/><path d="M13 16V5l7-2v11"/><ellipse cx="11" cy="16" rx="2.2" ry="1.7"/><ellipse cx="18" cy="14" rx="2.2" ry="1.7"/><path d="M13 8l7-2"/></svg></div>
    </div>
  </section>

  <!-- Pad 2: information -->
  <section class="pad pad--landing">
    <div class="pad-body"><div class="pad-scene" role="img" aria-label="Illustration of an airliner over an airport terminal and city skyline in yellow tones"></div></div>
    <div class="pad-panel">
      <div class="field field--select">Landing</div>
      <div class="field field--select">1.information</div>
      <div class="field">Notes</div>
      <div class="field field--select">Organ toccata</div>
      <div class="sound-btn"><svg width="22" height="20" viewBox="0 0 22 20" fill="none" stroke="#fff" stroke-width="1.4"><path d="M6 15V3l4 3"/><ellipse cx="4" cy="15" rx="2.2" ry="1.7"/><path d="M13 16V5l7-2v11"/><ellipse cx="11" cy="16" rx="2.2" ry="1.7"/><ellipse cx="18" cy="14" rx="2.2" ry="1.7"/><path d="M13 8l7-2"/></svg></div>
    </div>
    <div class="tower" style="left:89px;top:-37px;background:var(--tower-blue)"><svg width="26" height="26" viewBox="0 0 26 26" fill="none" stroke="#fff" stroke-width="1.1"><path d="M9 11h8l-1 3h-6z"/><path d="M10 14v10M16 14v10M8 24h10"/><path d="M13 11V8"/><path d="M11 7a3 3 0 014 0M9.5 5.5a5 5 0 017 0"/><path d="M2 9h4M4 7v4M20 9h4M22 7v4"/></svg></div>
  </section>

  <!-- Pad 3: caution -->
  <section class="pad pad--departure">
    <div class="pad-body"><div class="pad-scene" role="img" aria-label="Illustration of an airliner over an airport terminal and city skyline in green tones"></div></div>
    <div class="pad-panel">
      <div class="field field--select">Departure</div>
      <div class="field field--select">2. Caution</div>
      <div class="field">Notes</div>
      <div class="field field--select">Piano nocturne</div>
      <div class="sound-btn"><svg width="22" height="20" viewBox="0 0 22 20" fill="none" stroke="#fff" stroke-width="1.4"><path d="M6 15V3l4 3"/><ellipse cx="4" cy="15" rx="2.2" ry="1.7"/><path d="M13 16V5l7-2v11"/><ellipse cx="11" cy="16" rx="2.2" ry="1.7"/><ellipse cx="18" cy="14" rx="2.2" ry="1.7"/><path d="M13 8l7-2"/></svg></div>
    </div>
    <div class="tower" style="left:91px;top:-43px;background:var(--tower-navy)"><svg width="26" height="26" viewBox="0 0 26 26" fill="none" stroke="#fff" stroke-width="1.1"><path d="M9 11h8l-1 3h-6z"/><path d="M10 14v10M16 14v10M8 24h10"/><path d="M13 11V8"/><path d="M11 7a3 3 0 014 0M9.5 5.5a5 5 0 017 0"/><path d="M2 9h4M4 7v4M20 9h4M22 7v4"/></svg></div>
  </section>

  <!-- Pad 4: alert -->
  <section class="pad pad--alert">
    <div class="pad-body"><div class="pad-scene" role="img" aria-label="Illustration of an airliner over an airport terminal and city skyline in red tones"></div></div>
    <div class="pad-panel">
      <div class="field field--select">Moon</div>
      <div class="field field--select">3. Alert</div>
      <div class="field">Notes</div>
      <div class="field field--select">Bumblebee</div>
      <div class="sound-btn"><svg width="22" height="20" viewBox="0 0 22 20" fill="none" stroke="#222" stroke-width="1.4"><path d="M6 15V3l4 3"/><ellipse cx="4" cy="15" rx="2.2" ry="1.7"/><path d="M13 16V5l7-2v11"/><ellipse cx="11" cy="16" rx="2.2" ry="1.7"/><ellipse cx="18" cy="14" rx="2.2" ry="1.7"/><path d="M13 8l7-2"/></svg></div>
    </div>
    <div class="tower" style="left:103px;top:-38px;background:var(--gold)"><svg width="26" height="26" viewBox="0 0 26 26" fill="none" stroke="#fff" stroke-width="1.1"><path d="M9 11h8l-1 3h-6z"/><path d="M10 14v10M16 14v10M8 24h10"/><path d="M13 11V8"/><path d="M11 7a3 3 0 014 0M9.5 5.5a5 5 0 017 0"/><path d="M2 9h4M4 7v4M20 9h4M22 7v4"/></svg></div>
  </section>

  <footer class="footer">© Copyright 2021&nbsp; SKYNOTE &nbsp;&nbsp;|&nbsp;&nbsp; All Rights Reserved</footer>
</div>
</body>
</html>
```